Award winning Indie press looking for a world class book cover for global relaunch

We need to update a book cover for one of our titles which is being relaunched. The title will exist in both physical and e-formats.
The book is genre specific and era specific. World war 2, Greece. Beneath the Pale Hills is a compelling work of literary fiction, a war novel that explores the challenges of peace. A gripping historical adventure, it paints a portrait of courage and love in the fatal shadow of global conflict that has spilled into the twenty-first century.
Usage of the provided images is of course optional but it is a book about the German occupation of Greece. Images are public domain.
The cover needs to convey a sense of drama, typical for war novels.
Necessary information.
Size: A5
Title: Beneath the Pale Hills
Author: Martin Ashcombe
Blurb: An excellent book - Fairbridge Ledger UK
Publisher: logo- provided
Spine: Spine: 0.785 inches or 19.93 mm
Back cover text: Occupied Greece 1943. Beneath the Pale Hills is a compelling work of literary fiction, a war novel that also explores the challenges of peace. A gripping historical adventure, it paints a portrait of courage and love in the fatal shadow of global conflict that has spilled tragically into the twenty-first century.
Citizens of Nazi-occupied Greece face daily decisions that affect their freedom and their survival. When music teacher Stavros intervenes in a dispute between a Greek woman and a German soldier, he and jazz singer Irini are plunged into the brutal world of armed resistance.
Neil Hartwell, a British agent, lands in Northern Greece, where he joins Stavros’ and Irini’s network. Never fully understanding his Greek collaborators, he forms a deep bond with them.
In Scotland after World War Two, Neil is alienated from everyday life until he meets Judith, an up and coming intelligence officer. Surrounded by opportunity and courted by influential mentors, Neil and Judith learn that integrity has to be fought for in peacetime Britain just as in wartime Europe.
When Neil undertakes a final mission to Greece, now in the full throes of civil war, the weight of ideology and history descends with sudden force on the small town where former friends and enemies confront one another in a terrifying climax.
Please allow approximately 2cm height X 3 cm length for the bar code.
Reason: Decided to allow more time as this is proving a bit more tricky than expected.

```html
<!DOCTYPE html>
<html lang="en">
<head>
<meta charset="utf-8">
<title>Beneath the Pale Hills – Cover Spread</title>
<link rel="stylesheet" href="https://fonts.googleapis.com/css2?family=Fira+Sans+Condensed:wght@400;500;600;800&display=swap">
<style>
  :root {
    --sheet: #ffffff;
    --back-panel: #e9efee;
    --ink: #111111;
    --accent: #d8201f;
    --mark: #555555;
    --sky: #e6e6e6;
    --stone: #c4c4c4;
    --shadow-mid: #7c7c7c;
    --shadow-deep: #3a3a3a;
    --ground: #e2e2e2;
  }
  * { margin: 0; padding: 0; box-sizing: border-box; }
  html, body { width: 1200px; height: 857px; overflow: hidden; background: var(--sheet); }
  .spread {
    position: relative; width: 1200px; height: 857px;
    font-family: "Fira Sans Condensed", "Arial Narrow", sans-serif;
    color: var(--ink);
  }
  .crop-marks { position: absolute; inset: 0; }

  .back-cover {
    position: absolute; left: 172px; top: 140px; width: 401px; height: 612px;
    background: var(--back-panel);
  }
  .back-photo {
    position: absolute; left: 82px; top: 78px; width: 96px; height: 92px;
    background:
      radial-gradient(ellipse 60% 40% at 60% 60%, #4a4a4a 0%, rgba(74,74,74,0) 100%),
      linear-gradient(180deg, #e8e8e8 0%, #b8b8b8 50%, #8a8a8a 72%, #cfcfcf 100%);
  }
  .back-copy {
    position: absolute; left: 83px; top: 183px; width: 260px;
    font-size: 8.8px; font-weight: 500; line-height: 10.8px;
    text-align: justify; hyphens: auto;
  }
  .back-copy p + p { margin-top: 10.8px; }
  .publisher { position: absolute; left: 83px; top: 520px; }
  .publisher-label { font-size: 8px; font-weight: 600; line-height: 10px; }
  .publisher-name {
    display: flex; align-items: center; gap: 4px; margin-top: 5px;
    color: var(--accent); font-size: 12px; font-weight: 600; letter-spacing: 0.8px;
  }
  .publisher-name .square { width: 9px; height: 9px; background: var(--accent); }
  .barcode-area {
    position: absolute; left: 252px; top: 498px; width: 84px; height: 56px;
    border: 1px solid var(--ink);
  }

  .front-cover {
    position: absolute; left: 573px; top: 140px; width: 455px; height: 612px;
    overflow: hidden;
  }
  .front-photo {
    position: absolute; inset: 0;
    background:
      radial-gradient(ellipse 45% 38% at 82% 68%, var(--shadow-deep) 0%, rgba(58,58,58,0.55) 55%, rgba(58,58,58,0) 100%),
      radial-gradient(ellipse 30% 42% at 22% 55%, #505050 0%, rgba(80,80,80,0) 100%),
      radial-gradient(ellipse 28% 22% at 12% 92%, #f0f0f0 0%, rgba(240,240,240,0) 100%),
      linear-gradient(180deg, var(--sky) 0%, #dcdcdc 20%, var(--stone) 36%, #a6a6a6 50%, var(--shadow-mid) 66%, #a0a0a0 84%, var(--ground) 100%);
  }
  .endorsement {
    position: absolute; top: 34px; left: 0; width: 100%;
    text-align: center; color: var(--accent);
    font-size: 15px; font-weight: 400;
  }
  .title {
    position: absolute; top: 94px; left: 100px; width: 300px;
    text-align: center; font-weight: 800; line-height: 0.92; text-transform: uppercase;
    letter-spacing: -0.5px;
  }
  .title .line-one { display: block; font-size: 46px; }
  .title .line-two { display: block; font-size: 60px; }
  .author {
    position: absolute; top: 548px; left: 0; width: 100%;
    text-align: center; padding-left: 30px;
    font-size: 30px; font-weight: 500;
  }
</style>
</head>
<body>
<div class="spread">
  <svg class="crop-marks" width="1200" height="857" aria-hidden="true">
    <g stroke="var(--mark)" stroke-width="1">
      <line x1="186" y1="100" x2="186" y2="133"/>
      <line x1="573" y1="100" x2="573" y2="133"/>
      <line x1="627" y1="100" x2="627" y2="133"/>
      <line x1="1014" y1="100" x2="1014" y2="133"/>
      <line x1="186" y1="760" x2="186" y2="795"/>
      <line x1="573" y1="760" x2="573" y2="795"/>
      <line x1="627" y1="760" x2="627" y2="795"/>
      <line x1="1014" y1="760" x2="1014" y2="795"/>
      <line x1="132" y1="153" x2="165" y2="153"/>
      <line x1="132" y1="740" x2="165" y2="740"/>
      <line x1="1035" y1="153" x2="1068" y2="153"/>
      <line x1="1035" y1="740" x2="1068" y2="740"/>
    </g>
  </svg>

  <section class="back-cover">
    <div class="back-photo" role="img" aria-label="Black and white photograph of a tank on a city street in occupied Greece"></div>
    <div class="back-copy">
      <p>Occupied Greece 1943. Beneath the Pale Hills is a compelling work of literary fiction, a war novel that also explores the challenges of peace. A gripping historical adventure, it paints a portrait of courage and love in the fatal shadow of global conflict that has spilled tragically into the twenty-first century.</p>
      <p>Citizens of Nazi-occupied Greece face daily decisions that affect their freedom and their survival. When music teacher Stavros intervenes in a dispute between a Greek woman and a German soldier, he and jazz singer Irini are plunged into the brutal world of armed resistance.</p>
      <p>Neil Hartwell, a British agent, lands in Northern Greece, where he joins Stavros’ and Irini’s network. Never fully understanding his Greek collaborators, he forms a deep bond with them.</p>
      <p>In Scotland after World War Two, Neil is alienated from everyday life until he meets Judith, an up and coming intelligence officer. Surrounded by opportunity and courted by influential mentors, Neil and Judith learn that integrity has to be fought for in peacetime Britain just as in wartime Europe.</p>
      <p>When Neil undertakes a final mission to Greece, now in the full throes of civil war, the weight of ideology and history descends with sudden force on the small town where former friends and enemies confront one another in a terrifying climax.</p>
    </div>
    <div class="publisher">
      <div class="publisher-label">Published by:</div>
      <div class="publisher-name"><span class="square"></span>HALDEN</div>
    </div>
    <div class="barcode-area"></div>
  </section>

  <section class="front-cover">
    <div class="front-photo" role="img" aria-label="Dramatic black and white wartime photograph of occupying soldiers raising a war flag before ancient temple columns on a hilltop"></div>
    <p class="endorsement">An Excellent Book-Fairbridge Ledger UK</p>
    <h1 class="title"><span class="line-one">Beneath the</span><span class="line-two">Pale Hills</span></h1>
    <p class="author">Martin Ashcombe</p>
  </section>
</div>
</body>
</html>
```